I need graphics or illustrations to be used in a book and a power point presentation

I have created nine simple graphics using MS paint that were in blog articles. I now need to put these graphics in a book that I am publishing and also in a power point presentation.

I want these graphics to look more professional and consistent looking.

I have provided a word doc showing these graphics that need to be re-done

Industry/Entity Type

Paint

```html
<!DOCTYPE html>
<html lang="en">
<head>
<meta charset="utf-8">
<title>Gospel of Abraham Restored</title>
<link rel="stylesheet" href="https://fonts.googleapis.com/css2?family=Fira+Sans+Extra+Condensed:wght@500;600;700&display=swap">
<style>
  :root {
    --bg-blue: #0770b9;
    --title-yellow: #ffe600;
    --text-white: #ffffff;
    --gentile-top: #fffac4;
    --gentile-bottom: #fff200;
    --era-top: #d9edfb;
    --era-bottom: #a9d4f3;
    --ring-blue: #5fa0cc;
    --ring-edge: #8cbde0;
    --bar-border: #ffffff;
  }
  html, body {
    margin: 0;
    padding: 0;
    overflow: hidden;
    background: var(--bg-blue);
  }
  .timeline-chart {
    display: block;
    width: 1200px;
    height: 901px;
    font-family: "Fira Sans Extra Condensed", "Arial Narrow", sans-serif;
  }
  .chart-title {
    fill: var(--title-yellow);
    font-weight: 700;
    font-size: 44px;
  }
  .note {
    fill: var(--text-white);
    font-weight: 600;
    font-size: 24px;
  }
  .year {
    fill: var(--text-white);
    font-weight: 600;
    font-size: 25px;
  }
  .band-label {
    fill: #102a43;
    font-weight: 600;
    font-size: 25px;
  }
  .badge-label {
    fill: #1a2530;
    font-weight: 600;
    font-size: 23px;
  }
  .leader {
    stroke: var(--text-white);
    stroke-width: 1.5;
  }
</style>
</head>
<body>
<svg class="timeline-chart" viewBox="0 0 1200 901" xmlns="http://www.w3.org/2000/svg" aria-labelledby="chart-heading">
  <defs>
    <radialGradient id="pearl" cx="45%" cy="40%" r="65%">
      <stop offset="0%" stop-color="#ffffff"/>
      <stop offset="60%" stop-color="#eceeef"/>
      <stop offset="100%" stop-color="#b9bfc4"/>
    </radialGradient>
  </defs>

  <rect class="backdrop" width="1200" height="901" fill="var(--bg-blue)"/>

  <text id="chart-heading" class="chart-title" x="600" y="112" text-anchor="middle">Gospel of Abraham Restored</text>

  <!-- 1831 marker -->
  <line class="leader" x1="128" y1="174" x2="82" y2="440"/>
  <text class="note" x="396" y="180" text-anchor="middle">1831-4 the Fulness of the Gentiles comes in</text>
  <text class="note" x="396" y="212" text-anchor="middle">The Gentiles Reject the Fulness of the Gospel</text>

  <!-- 1836 marker -->
  <line class="leader" x1="264" y1="282" x2="235" y2="428"/>
  <text class="note" x="516" y="287" text-anchor="middle">1836-7 The Gospel of Abraham is Restored-</text>
  <text class="note" x="516" y="319" text-anchor="middle">God remembers his covenant with the</text>
  <text class="note" x="516" y="352" text-anchor="middle">House of Israel</text>

  <text class="year" x="84" y="465" text-anchor="middle">1831</text>
  <text class="year" x="243" y="465" text-anchor="middle">1836</text>
  <text class="note" x="516" y="462" text-anchor="middle">Four Generations</text>

  <!-- connectors below -->
  <line class="leader" x1="178" y1="584" x2="178" y2="630"/>
  <line class="leader" x1="754" y1="584" x2="844" y2="708"/>
  <line class="leader" x1="924" y1="584" x2="1068" y2="778"/>
  <line class="leader" x1="847" y1="480" x2="912" y2="400"/>

  <!-- timeline bands -->
  <g class="timeline-bar">
    <rect x="79" y="481" width="175" height="52" fill="var(--gentile-top)"/>
    <rect x="79" y="533" width="175" height="51" fill="var(--gentile-bottom)"/>
    <rect x="254" y="481" width="500" height="52" fill="var(--era-top)"/>
    <rect x="254" y="533" width="500" height="51" fill="var(--era-bottom)"/>
    <rect x="754" y="481" width="168" height="52" fill="var(--gentile-top)"/>
    <rect x="754" y="533" width="168" height="51" fill="var(--gentile-bottom)"/>
    <rect x="922" y="481" width="210" height="52" fill="var(--era-top)"/>
    <rect x="922" y="533" width="210" height="51" fill="var(--era-bottom)"/>
    <rect x="79" y="481" width="1053" height="103" fill="none" stroke="var(--bar-border)" stroke-width="4"/>
    <line x1="254" y1="481" x2="254" y2="584" stroke="var(--bar-border)" stroke-width="4"/>
    <line x1="754" y1="481" x2="754" y2="584" stroke="var(--bar-border)" stroke-width="4"/>
    <line x1="922" y1="481" x2="922" y2="584" stroke="var(--bar-border)" stroke-width="4"/>

    <text class="band-label" x="166" y="538" text-anchor="middle">Gentiles</text>
    <text class="band-label" x="500" y="538" text-anchor="middle">Dispensation of the Gospel of Abraham</text>
    <text class="band-label" x="835" y="538" text-anchor="middle">Gentiles</text>
    <text class="band-label" x="1031" y="524" text-anchor="middle">Scattered</text>
    <text class="band-label" x="1031" y="554" text-anchor="middle">Remnants</text>
  </g>

  <!-- word badge -->
  <g class="badge badge-word">
    <circle cx="178" cy="697" r="108" fill="var(--ring-blue)" stroke="var(--ring-edge)" stroke-width="2"/>
    <circle cx="178" cy="697" r="73" fill="url(#pearl)"/>
    <text class="badge-label" x="178" y="695" text-anchor="middle">Gospel</text>
    <text class="badge-label" x="178" y="721" text-anchor="middle">delivered</text>
    <text class="badge-label" x="178" y="747" text-anchor="middle">in WORD</text>
  </g>

  <!-- word power deed badge -->
  <g class="badge badge-power">
    <circle cx="931" cy="334" r="77" fill="var(--ring-blue)" stroke="var(--ring-edge)" stroke-width="2"/>
    <circle cx="931" cy="334" r="59" fill="url(#pearl)"/>
    <text class="badge-label" x="931" y="299" text-anchor="middle" font-size="21">Gospel</text>
    <text class="badge-label" x="931" y="325" text-anchor="middle" font-size="21">delivered in</text>
    <text class="badge-label" x="931" y="351" text-anchor="middle" font-size="21">WORD-POWER</text>
    <text class="badge-label" x="931" y="377" text-anchor="middle" font-size="21">-DEED</text>
  </g>

  <text class="note" x="516" y="614" text-anchor="middle">Knowledge of Gospel</text>
  <text class="note" x="516" y="646" text-anchor="middle">taken to House of Israel</text>
  <text class="note" x="610" y="733" text-anchor="middle" font-size="25">The Times of the Gentiles comes in again</text>
  <text class="note" x="788" y="803" text-anchor="middle" font-size="25">The Remnant of Israel is gathered and redeemed</text>
</svg>
</body>
</html>
```